Window Graphics for New Dental Office

This is a bank of windows along a busy street that a new dental office wants to cover in graphics. The file ideas for window designs is the look the client is going for. The template with bleed lines .pdf is a a 10 percent scaled version of the graphics for the graphic layout. The dental window placement diagram is a picture showing the actual windows that will be covered in light green and the other .pdf is the clients logo.

This dentist wants a high end botique look with an competent and inviting feel.

You may incorporate ideas like:
- Emergency and Same Day Appointments Available
- The lead dentist works with every patient
- latest technology for crowns and veneers in-house
- free teeth whitening kit with every expert consultation
- every patient is our best patient
- Financing available
- PPO insurance and Payment Plans Accepted

```html
<!DOCTYPE html>
<html lang="en">
<head>
<meta charset="utf-8">
<title>Crestline Dental Studio – Window Graphics</title>
<link href="https://fonts.googleapis.com/css2?family=Poppins:wght@400;600&display=swap" rel="stylesheet">
<style>
  :root {
    --backdrop: #bdbdbd;
    --header-plum: #5b4e63;
    --sky-blue: #2eaae1;
    --deep-blue: #0b62ad;
    --logo-blue: #1266b0;
    --white: #ffffff;
  }
  * { box-sizing: border-box; margin: 0; padding: 0; }
  html, body { width: 1200px; height: 457px; overflow: hidden; }
  body {
    position: relative;
    background: var(--backdrop);
    font-family: "Poppins", sans-serif;
    color: var(--white);
  }
  .header-band {
    position: absolute; left: 102px; top: 98px; width: 996px; height: 66px;
    background: var(--header-plum);
  }
  .brand-plate {
    position: absolute; left: 494px; top: 101px; width: 195px; height: 60px;
    background: var(--white);
    display: flex; align-items: center; justify-content: center; gap: 8px;
  }
  .brand-mark { width: 12px; height: 12px; background: var(--logo-blue); }
  .brand-name {
    color: var(--logo-blue); font-weight: 600; font-size: 13px; line-height: 1.15;
    letter-spacing: 0.02em; text-transform: uppercase;
  }
  .panel { position: absolute; }
  .panel--sky { background: var(--sky-blue); }
  .panel--deep { background: var(--deep-blue); }
  .panel-copy { position: absolute; font-size: 11px; line-height: 13px; }
  .panel-copy strong { font-weight: 600; }
  .divider { display: block; width: 24px; height: 1px; background: var(--white); margin: 9px 0 11px; }
  .photo { position: absolute; }
  .photo--exam {
    left: 245.5px; top: 164px; width: 136px; height: 141px;
    background: linear-gradient(135deg, #d9d6d4 0%, #e8b8a4 45%, #c96a6a 70%, #a9d3dc 100%);
  }
  .photo--smile {
    left: 385px; top: 164px; width: 417px; height: 191px;
    background: radial-gradient(ellipse 55% 40% at 50% 50%, #e07a86 0%, #d98c86 45%, #deae95 75%, #e7c4ad 100%);
  }
</style>
</head>
<body>
  <div class="header-band"></div>
  <div class="brand-plate">
    <span class="brand-mark"></span>
    <span class="brand-name">Crestline<br>Dental Studio</span>
  </div>

  <!-- column: appointments -->
  <div class="panel panel--sky" style="left:102.5px;top:164px;width:126px;height:141px;">
    <p class="panel-copy" style="left:13px;top:20px;">
      <strong>EMERGENCY</strong><br>and <strong>Same Day<br>Appointments</strong><br>Available
      <span class="divider"></span>
      The <strong>Lead Dentist</strong><br>works with<br><strong>every patient</strong>
    </p>
  </div>
  <div class="panel panel--deep" style="left:102.5px;top:309px;width:126px;height:46px;"></div>

  <!-- column: technology -->
  <div class="photo photo--exam" role="img" aria-label="Photo of a young patient at a dental check-up with a mouth mirror"></div>
  <div class="panel panel--sky" style="left:245.5px;top:309px;width:136px;height:46px;">
    <p class="panel-copy" style="left:16px;top:3px;line-height:12px;">
      Latest <strong>technology</strong><br>for <strong>crowns</strong> and<br><strong>veneers in-house</strong>
    </p>
  </div>

  <!-- centre: smile -->
  <div class="photo photo--smile" role="img" aria-label="Close-up photo of a smile showing teeth before and after whitening"></div>

  <!-- column: whitening -->
  <div class="panel panel--deep" style="left:804.5px;top:164px;width:136px;height:141px;">
    <p class="panel-copy" style="left:26px;top:46px;">
      <strong>Free teeth<br>whitening kit</strong><br>with every expert<br>consultation
    </p>
  </div>
  <div class="panel panel--sky" style="left:804.5px;top:309px;width:136px;height:46px;">
    <p class="panel-copy" style="left:18px;top:11px;">
      <strong>Every patient</strong> is<br>our <strong>best patient</strong>
    </p>
  </div>

  <!-- column: financing -->
  <div class="panel panel--sky" style="left:957px;top:164px;width:140px;height:141px;">
    <p class="panel-copy" style="left:24px;top:25px;">
      <strong>FINANCING<br>AVAILABLE</strong>
      <span class="divider" style="margin:17px 0 12px;"></span>
      <strong>PPO insurance</strong><br>and <strong>Payment<br>Plans</strong> Accepted
    </p>
  </div>
  <div class="panel panel--deep" style="left:957px;top:309px;width:140px;height:46px;"></div>
</body>
</html>
```